Geschäftspapiere für Malerfirma
Zielgruppe
Malerfirma für hochwertige Kundschaft.
Wir verarbeiten besondes hochpigmentierte Farben und hochwertigen Tapeten.
Aufgabenstellung
Unser neues Motto ist ,, Aus Liebe zu unserer Berufung'
Wir führen viele Tapezierarbeiten aus ... etwas mit einem Tapetenmuster (Muster aus dem Firmenlogo) finde ich schon ansprechend.

```html
<!DOCTYPE html>
<html lang="de">
<head>
<meta charset="utf-8">
<title>Briefbogen Malermeister</title>
<link href="https://fonts.googleapis.com/css2?family=Arimo&family=Open+Sans:wght@400;600&family=PT+Sans+Narrow&display=swap" rel="stylesheet">
<style>
  :root {
    --backdrop: #d9d8d8;
    --paper: #f1f1f1;
    --leaf-green: #6d8744;
    --plum: #7b4c57;
    --warm-brown: #8b6b62;
    --ink: #1d1d1d;
    --body-grey: #5a5a5a;
    --mark-grey: #b8b8b8;
  }
  * { margin: 0; padding: 0; box-sizing: border-box; }
  html, body { width: 1119px; height: 1200px; overflow: hidden; background: var(--backdrop); }
  .stage { position: relative; width: 1119px; height: 1200px; }
  .letterhead {
    position: absolute; left: 155px; top: 30px;
    width: 863px; height: 1216px;
    transform: scale(0.9375); transform-origin: top left;
    background: var(--paper);
    box-shadow: 0 10px 30px rgba(0,0,0,.18);
    overflow: hidden;
    font-family: "Arimo", Arial, sans-serif;
  }
  .band { position: absolute; left: 0; width: 863px; }
  .band--top { top: 0; height: 170px; }
  .band--bottom { bottom: 0; height: 120px; }
  .brand-name {
    position: absolute; left: 88px; top: 48px;
    font-family: "Open Sans", sans-serif; font-weight: 600;
    font-size: 24px; line-height: 30px; color: #ffffff; white-space: nowrap;
  }
  .motto {
    position: absolute; left: 292px; top: 86px;
    font-family: "Open Sans", sans-serif; font-size: 19px; line-height: 24px; color: var(--ink);
    white-space: nowrap;
    transform: rotate(4deg); transform-origin: left center;
  }
  .window-marks { position: absolute; left: 42px; top: 195px; width: 348px; height: 182px; }
  .sender-line {
    position: absolute; left: 62px; top: 222px;
    font-family: "PT Sans Narrow", sans-serif; font-size: 12px; color: var(--ink);
  }
  .sender-line .firm { color: var(--warm-brown); }
  .recipient {
    position: absolute; left: 63px; top: 268px;
    font-family: "PT Sans Narrow", sans-serif; font-size: 16.5px; line-height: 21px; color: var(--ink);
  }
  .letter-body {
    position: absolute; left: 65px; top: 478px; width: 720px;
    font-size: 16px; line-height: 20.5px; color: var(--body-grey);
  }
  .letter-body p { margin-bottom: 20.5px; }
  .letter-body .closing { margin-top: 40px; margin-bottom: 40px; }
  .letter-body .greeting { margin-bottom: 40px; }
  .fold-mark { position: absolute; left: 0; top: 923px; width: 12px; height: 1px; background: var(--mark-grey); }
  .footer { position: absolute; top: 1085px; font-size: 14px; line-height: 18px; color: var(--ink); }
  .footer--address { left: 47px; top: 1088px; }
  .footer--address .name { color: var(--warm-brown); }
  .footer--contact { left: 191px; font-size: 13px; width: 235px; }
  .contact-row { display: flex; align-items: center; gap: 10px; height: 17.7px; white-space: nowrap; }
  .contact-row svg { width: 15px; height: 13px; flex: none; }
  .footer--bank { left: 436px; top: 1082px; }
</style>
</head>
<body>
<div class="stage">
  <div class="letterhead">
    <svg class="band band--top" viewBox="0 0 863 170" role="img" aria-label="Tapetenmuster mit grünen Rautenornamenten">
      <path d="M0 0 H863 V160 C760 95 650 72 540 74 C400 78 260 110 0 118 Z" fill="var(--leaf-green)"/>
    </svg>
    <div class="brand-name">Jonas Wehrmann</div>
    <div class="motto">„Aus Liebe zu unserer Berufung „</div>

    <svg class="window-marks" viewBox="0 0 348 182" fill="none" stroke="var(--mark-grey)" stroke-width="1.5">
      <path d="M0 20 V1 H24"/><path d="M324 1 H347 V20"/>
      <path d="M0 162 V181 H24"/><path d="M324 181 H347 V162"/>
    </svg>
    <div class="sender-line"><span class="firm">JONAS WEHRMANN GmbH |</span> Lindenweg 48 * 10245 Berlin</div>
    <div class="recipient">Herrn<br>Max Mustermann<br>Musterstrasse</div>

    <div class="letter-body">
      <p>Sehr geehrter Herr Lorenz,</p>
      <p>Die HKF Netz GmbH ist eine Servicegesellschaft für qualifizierteBaufinanzierungsberater<br>in ganz Deutschland.Als Kompetenzzentrumder Immobilienfinanzierung bieten<br>die angeschlossenen Partner qualifizierte Baufinanzierungsberatung zu besten Konditionen<br>&nbsp;unser unserer Marke “Wohnkredit-Kompass”.</p>
      <p>Die Partner des HKF sind Teil eines des größten freien überregionalen und unabhängigen<br>Baufinanzierungsvermittlernetzwerkes in Deutschland. Wir erstellen für Sie aus dem Angebot<br>von über 100 Banken,Versicherungen und Bausparkassen ein maßgeschneidertes<br>Finanzierungskonzept mit Top-Konditionen. Gleichzeitig loten wir für Sie regionale und<br>überregionale Fördermittelmöglichkeiten auf Basis Ihrer individuellen Situation aus.<br>Und das Beste daran: Wir arbeiten wirklich unabhängig!</p>
      <p class="closing">Für Rückfragen stehe ich Ihnen gerne zur Verfügung.</p>
      <p class="greeting">Mit freundlichen Grüßen</p>
      <p>Max Mustermann</p>
    </div>
    <div class="fold-mark"></div>

    <div class="footer footer--address"><span class="name">Jonas Wehrmann</span><br>Lindenweg 48<br>10245 Berlin<br>Germany</div>
    <div class="footer footer--contact">
      <div class="contact-row"><svg viewBox="0 0 15 13"><path d="M1 4 Q7.5 -1 14 4 L12 6 L10 4 H5 L3 6 Z M3 7 H12 V12 H3 Z" fill="var(--body-grey)"/></svg>030/48206617</div>
      <div class="contact-row"><svg viewBox="0 0 15 13"><rect x="4" y="1" width="7" height="4" fill="var(--body-grey)"/><rect x="1" y="5" width="13" height="7" rx="1" fill="var(--body-grey)"/></svg>030/48206619</div>
      <div class="contact-row"><svg viewBox="0 0 15 13"><rect x="4.5" y="0.5" width="6" height="12" rx="1" fill="none" stroke="var(--body-grey)" stroke-width="1.2" transform="rotate(-15 7.5 6.5)"/></svg>0176/39152804</div>
      <div class="contact-row"><svg viewBox="0 0 15 13"><rect x="1" y="2" width="13" height="9" fill="var(--body-grey)"/><path d="M1 2 L7.5 7 L14 2" fill="none" stroke="var(--paper)" stroke-width="1"/></svg>maler-wehrmann@pinselpost.de</div>
    </div>
    <div class="footer footer--bank">USt-IdNr.:DE518604239<br>Steuernummer 137/418/00263<br>IBAN AT41 2806 1000 0073 4412<br>BIC LNDBAT2K118</div>

    <svg class="band band--bottom" viewBox="0 0 863 120" role="img" aria-label="Tapetenmuster mit pflaumenfarbenen Rautenornamenten">
      <path d="M0 78 C200 98 420 100 600 82 C720 68 800 35 863 12 V120 H0 Z" fill="var(--plum)"/>
    </svg>
  </div>
</div>
</body>
</html>
```